Bref créative
Contract folder, Biz Card,Letter head, Fax Cov, Env,A4 Env,CD Cov&Pack,PPT
Email Sign, scratch paper
Professional
Harvinder Pal Okoro
Director
Vel Metrics Systems Private Limited
Plot No. 217 Industrial Growth Zone Phase 4 Distt- Kelmar 174 398, Punjab, India
hokoro@velmetrics.example
www.VelMetrics.example
on letter head & envelops we would prefer to mention the manufacturers we represent on Letter Head, Biz Card, A4 Env.
1) Brovane Instruments 2) Tollwick Fendor 3) Mo-Ve-Sel 4) Dovin
5) TUVO 6) Plazor 7) Orvix 8) Universal Prism Workshops 9) KV Fabrications 10) Tolbry Chemical 11) MaxiSp 12) DOR Scientific 13) VextaMol 14) KPL
1) use only logo
2) write official email info@velmetrics.example & website www.VelMetrics.example
3) Write in small "Suppliers of Chromatography Consumables & Spectroscopy Supplies"
WE ARE OPEN TO IDEAS
Vel Metrics System Private Limited Logo
vms id card sample content
logo eps format

```html
<!DOCTYPE html>
<html lang="en">
<head>
<meta charset="utf-8">
<title>Vel Metrics Systems – Business Card</title>
<link rel="stylesheet" href="https://fonts.googleapis.com/css2?family=Open+Sans:wght@400;600;700&display=swap">
<style>
  :root {
    --stage: #e9ecef;
    --card-white: #ffffff;
    --brand-blue: #1a86d6;
    --brand-blue-dark: #0c5fa8;
    --band-blue: #2b8fdc;
    --band-grey: #eef1f4;
    --accent-red: #e02828;
    --ink: #3a3f45;
    --ink-soft: #6c737a;
    --rule: #d5dbe1;
    --white: #ffffff;
  }
  * { box-sizing: border-box; margin: 0; padding: 0; }
  html, body { width: 1200px; height: 775px; overflow: hidden; }
  body {
    background: var(--stage);
    font-family: "Open Sans", Arial, sans-serif;
    position: relative;
  }
  .card {
    position: absolute;
    top: 237px;
    width: 520px;
    height: 300px;
    border-radius: 16px;
    overflow: hidden;
    box-shadow: 0 6px 18px rgba(0,0,0,.18);
  }

  /* ---------- Front ---------- */
  .card--front { left: 50px; background: var(--card-white); }
  .name-band { position: absolute; left: 210px; top: 22px; right: 0; height: 54px; }
  .name-band__red {
    position: absolute; left: -10px; top: 0; width: 6px; height: 36px;
    background: var(--accent-red);
  }
  .name-band__name {
    height: 36px; background: var(--band-blue); color: var(--white);
    font-size: 17px; font-weight: 600; line-height: 36px; padding-left: 12px;
  }
  .name-band__title {
    height: 18px; background: var(--band-grey); color: var(--ink-soft);
    font-size: 10px; line-height: 18px; padding-left: 12px;
  }
  .divider {
    position: absolute; left: 206px; top: 96px; width: 1px; height: 170px;
    background: var(--rule);
  }
  .company {
    position: absolute; left: 222px; top: 96px; width: 280px;
    color: var(--ink); font-size: 9.5px; line-height: 1.45;
  }
  .company__name { color: var(--brand-blue-dark); font-weight: 700; font-size: 10px; }
  .contact {
    position: absolute; left: 222px; top: 160px; width: 280px;
    font-size: 9px; line-height: 1.6; color: var(--ink);
  }
  .contact dt { float: left; width: 42px; color: var(--brand-blue-dark); font-weight: 600; }
  .contact dd { margin-left: 42px; }

  .brand-name {
    position: absolute; left: 30px; top: 150px; width: 162px;
    font-size: 24px; font-weight: 600; color: var(--brand-blue);
    line-height: 1.2;
  }
  .partners {
    position: absolute; left: 30px; top: 204px; width: 162px;
    border-top: 2px solid var(--accent-red); padding-top: 5px;
    font-size: 6.5px; line-height: 1.4; color: var(--ink-soft);
    columns: 2; column-gap: 8px;
  }
  .partners li { list-style: none; white-space: nowrap; }

  /* ---------- Back ---------- */
  .card--back {
    left: 630px;
    background: radial-gradient(ellipse at 45% 40%, #3aa2ea 0%, var(--brand-blue) 45%, var(--brand-blue-dark) 100%);
    color: var(--white);
  }
  .back-brand-name {
    position: absolute; left: 0; right: 0; top: 108px; text-align: center;
    font-size: 32px; font-weight: 600; color: var(--white); line-height: 1.2;
  }
  .back-tagline {
    position: absolute; left: 0; right: 0; top: 232px; text-align: center;
    font-size: 8.5px; line-height: 1.6; color: var(--white);
  }
</style>
</head>
<body>

<section class="card card--front" aria-label="Business card front">
  <div class="name-band">
    <span class="name-band__red"></span>
    <div class="name-band__name">Harvinder Pal Okoro</div>
    <div class="name-band__title">Director</div>
  </div>

  <div class="divider"></div>

  <div class="company">
    <p class="company__name">Vel Metrics Systems Private Limited</p>
    <p>Plot No. 217 Industrial Growth Zone Phase 4</p>
    <p>Distt- Kelmar 174 398, Punjab, India</p>
  </div>

  <dl class="contact">
    <dt>Phone</dt><dd>+91 172 555 0148</dd>
    <dt>Cell</dt><dd>+91 98765 01234</dd>
    <dt>Fax</dt><dd>+91 172 555 0149</dd>
    <dt>E-mail</dt><dd>hokoro@velmetrics.example</dd>
    <dt>Web</dt><dd>www.VelMetrics.example</dd>
  </dl>

  <p class="brand-name">VelMetrics</p>

  <ul class="partners">
    <li>Brovane Instruments</li>
    <li>Tollwick Fendor</li>
    <li>Mo-Ve-Sel</li>
    <li>Dovin</li>
    <li>TUVO</li>
    <li>Plazor</li>
    <li>Orvix</li>
    <li>Universal Prism Workshops</li>
    <li>KV Fabrications</li>
    <li>Tolbry Chemical</li>
    <li>MaxiSp</li>
    <li>DOR Scientific</li>
    <li>VextaMol</li>
    <li>KPL</li>
  </ul>
</section>

<section class="card card--back" aria-label="Business card back">
  <p class="back-brand-name">VelMetrics</p>
  <div class="back-tagline">
    <p>Suppliers of Chromatography Consumables &amp; Spectroscopy Supplies</p>
    <p>Email: info@velmetrics.example &nbsp;|&nbsp; Web: www.VelMetrics.example</p>
  </div>
</section>

</body>
</html>
```